Hadley & Partners, LLC Business Card 2016

We need a new business card design for a very important trade show coming up.

We are a compliance Consulting Firm. Our clients are stock brokerage firms and investment advisers.

I would like our logo on both sides of the card.

Info in the front of the card shold include:

Logo
First & Last Name
Title
Office #
Cell #
Email
Company Address (42 W. Calloway St., Suite 300 Pasadena, CA 91417

Back of the card should include the logo and url: www.hadleypartnersgroup.com

Target Market(s)

Stock Brokerage Firms and Investment Advisers

Industry/Entity Type

Financial Service

Contact Information for Business Card

Marcus J. Pellew
President
42 W. Calloway St., Suite 300
Pasadena, CA 91417
O 626.555.0147 ext. 204
C 818.555.0193
Email: marcus@hadleypartnersgroup.com
www.hadleypartnersgroup.com

Requirements
Nice to have
• The back of the card could be black with the logo with the white letters.
• I do want the front of the card to at least have the color logo with the black "Hadley & Partners Lettering.

```html
<!DOCTYPE html>
<html lang="en">
<head>
<meta charset="utf-8">
<title>Hadley &amp; Partners, LLC — Business Card</title>
<link rel="stylesheet" href="https://fonts.googleapis.com/css2?family=Cinzel:wght@400;600&family=Open+Sans:wght@400;600&display=swap">
<style>
  :root {
    --stage: #e6e6e4;
    --card-white: #ffffff;
    --card-black: #161616;
    --ink: #1d1d1d;
    --accent: #d0161b;
    --paper-white: #f4f4f4;
    --shadow: 0 10px 28px rgba(0,0,0,0.22);
  }
  * { box-sizing: border-box; margin: 0; padding: 0; }
  html, body {
    width: 1200px; height: 1021px; overflow: hidden;
    background: var(--stage);
  }
  .sheet {
    width: 1200px; height: 1021px;
    display: flex; align-items: center; justify-content: center; gap: 40px;
  }
  .card {
    width: 540px; height: 309px;
    box-shadow: var(--shadow);
    position: relative;
    overflow: hidden;
  }
  .card--front { background: var(--card-white); }
  .card--back {
    background: var(--card-black);
    display: flex; flex-direction: column; align-items: center; justify-content: center;
  }

  .brand {
    display: flex; align-items: center; gap: 9px;
    font-family: "Cinzel", serif; font-weight: 600;
  }
  .brand__square { width: 22px; height: 22px; background: var(--accent); flex: none; }
  .brand__name { color: var(--ink); font-size: 14px; letter-spacing: 0.3px; white-space: nowrap; }

  .card--front .brand { position: absolute; left: 30px; top: 143px; }

  .card--back .brand { flex-direction: column; gap: 20px; }
  .card--back .brand__square { width: 64px; height: 64px; }
  .card--back .brand__name { color: var(--paper-white); font-size: 36px; letter-spacing: 1px; }
  .back__url {
    margin-top: 16px;
    font-family: "Open Sans", sans-serif; font-size: 13px;
    color: var(--paper-white); letter-spacing: 0.5px;
  }

  .contact {
    position: absolute; left: 252px; top: 56px;
    font-family: "Open Sans", sans-serif; color: var(--ink);
  }
  .contact__name {
    font-family: "Cinzel", serif; font-weight: 400; font-size: 19px;
    letter-spacing: 0.5px; color: var(--ink); white-space: nowrap;
  }
  .contact__first { color: var(--accent); }
  .contact__title { font-size: 13px; font-weight: 600; color: var(--accent); margin-bottom: 14px; }
  .contact__list { list-style: none; }
  .contact__item {
    display: flex; gap: 10px; align-items: flex-start;
    font-size: 12px; line-height: 17px; margin-bottom: 5px; white-space: nowrap;
  }
  .contact__item svg { width: 11px; height: 11px; margin-top: 3px; flex: none; fill: var(--accent); }
  .contact__item--web { color: var(--accent); }
</style>
</head>
<body>
<main class="sheet">

  <section class="card card--front" aria-label="Card front">
    <div class="brand">
      <span class="brand__square"></span>
      <span class="brand__name">Hadley &amp; Partners</span>
    </div>

    <div class="contact">
      <p class="contact__name"><span class="contact__first">Marcus J.</span> Pellew</p>
      <p class="contact__title">Job Title</p>
      <ul class="contact__list">
        <li class="contact__item">
          <svg viewBox="0 0 12 12"><path d="M6 0a4 4 0 0 0-4 4c0 3 4 8 4 8s4-5 4-8a4 4 0 0 0-4-4zm0 5.6A1.6 1.6 0 1 1 6 2.4a1.6 1.6 0 0 1 0 3.2z"/></svg>
          <span>42 W. Calloway St., Suite 300<br>Pasadena, CA 91417</span>
        </li>
        <li class="contact__item">
          <svg viewBox="0 0 12 12"><path d="M1 3c0-1 1-2 5-2s5 1 5 2v1H8V3H4v1H1zM3 5h6l2 3v3H1V8zm3 1.5a1.5 1.5 0 1 0 0 3 1.5 1.5 0 0 0 0-3z"/></svg>
          <span>626.555.0147 ext. 204</span>
        </li>
        <li class="contact__item">
          <svg viewBox="0 0 12 12"><path d="M3.5 0h5a1 1 0 0 1 1 1v10a1 1 0 0 1-1 1h-5a1 1 0 0 1-1-1V1a1 1 0 0 1 1-1zm.5 1.5v7.5h4V1.5zM6 9.8a.7.7 0 1 0 0 1.4.7.7 0 0 0 0-1.4z"/></svg>
          <span>818.555.0193</span>
        </li>
        <li class="contact__item">
          <svg viewBox="0 0 12 12"><path d="M0 2h12v1L6 7 0 3zm0 2.3 6 4 6-4V10H0z"/></svg>
          <span>marcus@hadleypartnersgroup.com</span>
        </li>
        <li class="contact__item contact__item--web">
          <svg viewBox="0 0 12 12"><path d="M6 0a6 6 0 1 0 0 12A6 6 0 0 0 6 0zm0 1.2c.7.8 1.2 2 1.4 3.3H4.6C4.8 3.2 5.3 2 6 1.2zM1.3 5.5h2.2c0 .4 0 .7.1 1H1.3a4.8 4.8 0 0 1 0-1zm.4 2.2h2.1c.2 1 .5 1.9 1 2.6a4.8 4.8 0 0 1-3.1-2.6zm4.3 3.1c-.7-.8-1.1-1.9-1.3-3.1h2.6c-.2 1.2-.6 2.3-1.3 3.1zm1.4-.5c.5-.7.8-1.6 1-2.6h2.1a4.8 4.8 0 0 1-3.1 2.6zm1.2-3.8c.1-.3.1-.6.1-1h2.2a4.8 4.8 0 0 1 0 1z"/></svg>
          <span>www.hadleypartnersgroup.com</span>
        </li>
      </ul>
    </div>
  </section>

  <section class="card card--back" aria-label="Card back">
    <div class="brand">
      <span class="brand__square"></span>
      <span class="brand__name">Hadley &amp; Partners</span>
    </div>
    <p class="back__url">www.hadleypartnersgroup.com</p>
  </section>

</main>
</body>
</html>
```